New Business Card Design Project

New business card design required for an electrical business in Australia. Offering quality electrical services including design and installation. Electrical services offered are domestic, commercial and industrial. Also meets all the air conditioning installation and maintenance needs.

Target Market(s)

The business is sleek, professional and caters primarily to wealthy clients and government contracts looking for exceptional, tailored service.

Industry/Entity Type

Electrical

Contact Information for Business Card

Damian Corlowe (Director)
0438 615 274
admin@vrtelectrical.com.au
www.vrtelectrical.com.au

Font styles to use
Sans Serif

Requirements
Must have
• The business card must show the license number - 64193 to comply with legislation.
Nice to have
• The logo colours and fonts could be incorporated into the design if the designer sees fit. We are open to new ideas and welcome creativity. The logo style guide is attached for reference if required.

```html
<!DOCTYPE html>
<html lang="en">
<head>
<meta charset="utf-8">
<title>VRT Electrical – Business Card</title>
<link rel="stylesheet" href="https://fonts.googleapis.com/css2?family=Open+Sans:ital,wght@0,400;0,700;1,400&family=Noto+Serif:wght@400&display=swap">
<style>
  :root {
    --navy: #142c57;
    --navy-dark: #0f2347;
    --grey: #6f6f71;
    --grey-light: #a9a9ab;
    --paper: #ffffff;
    --stage: #2b2d31;
    --ink: #2f3136;
  }
  * { box-sizing: border-box; margin: 0; padding: 0; }
  html, body { width: 1200px; height: 900px; overflow: hidden; }
  body {
    background: var(--stage);
    font-family: "Open Sans", sans-serif;
    position: relative;
  }
  .card {
    position: absolute;
    top: 285px;
    width: 540px;
    height: 330px;
    overflow: hidden;
    box-shadow: 0 10px 30px rgba(0,0,0,.45);
  }
  .card--front { left: 40px; background: var(--paper); }
  .card--back { left: 620px; background: var(--navy); }

  .corner-tab {
    position: absolute; left: 0; top: 0;
    width: 14px; height: 34px; background: var(--grey);
  }
  .corner-band { position: absolute; left: 0; bottom: 0; }

  .person { position: absolute; left: 36px; top: 30px; }
  .person__name {
    font-weight: 700; font-size: 17px; letter-spacing: .5px;
    color: var(--navy); text-transform: uppercase;
  }
  .person__role {
    font-style: italic; font-size: 13px; color: var(--grey); margin-top: 1px;
  }

  .contacts { position: absolute; left: 36px; top: 100px; list-style: none; }
  .contacts__item {
    display: flex; align-items: center; gap: 10px;
    font-family: "Noto Serif", serif; font-size: 13.5px; color: var(--ink);
    margin-bottom: 9px; white-space: nowrap;
  }
  .contacts__icon {
    width: 22px; height: 22px; flex: none;
    border: 1.5px solid var(--navy); border-radius: 5px;
    display: flex; align-items: center; justify-content: center;
  }
  .licence {
    position: absolute; left: 36px; top: 200px;
    font-size: 11.5px; color: var(--grey); letter-spacing: .3px; white-space: nowrap;
  }
  .licence strong { color: var(--navy); font-weight: 700; }

  .brand {
    position: absolute; display: flex; align-items: center; gap: 12px;
    font-family: "Open Sans", sans-serif; font-weight: 700;
    text-transform: uppercase; white-space: nowrap;
  }
  .brand--front {
    left: 270px; top: 250px; color: var(--navy);
    font-size: 22px; letter-spacing: 2px;
  }
  .brand--back {
    left: 50%; top: 50%; transform: translate(-50%,-50%);
    color: var(--paper); font-size: 32px; letter-spacing: 3px;
  }
  .brand__dot { width: 12px; height: 12px; border-radius: 50%; background: currentColor; flex: none; }
</style>
</head>
<body>

<section class="card card--front" aria-label="Business card front">
  <div class="corner-tab"></div>
  <svg class="corner-band" width="120" height="110" viewBox="0 0 120 110" aria-hidden="true">
    <polygon points="0,0 10,0 10,110 0,110" fill="var(--navy)"/>
    <polygon points="10,40 40,40 120,110 10,110" fill="var(--grey-light)"/>
    <polygon points="10,40 22,40 22,110 10,110" fill="var(--navy-dark)"/>
  </svg>

  <div class="person">
    <p class="person__name">Damian Corlowe</p>
    <p class="person__role">Director</p>
  </div>

  <ul class="contacts">
    <li class="contacts__item">
      <span class="contacts__icon">
        <svg width="12" height="12" viewBox="0 0 24 24" aria-hidden="true"><path fill="var(--navy)" d="M6.6 10.8a15 15 0 0 0 6.6 6.6l2.2-2.2c.3-.3.7-.4 1-.2 1.1.4 2.3.6 3.6.6.6 0 1 .4 1 1V20c0 .6-.4 1-1 1A17 17 0 0 1 3 4c0-.6.4-1 1-1h3.5c.6 0 1 .4 1 1 0 1.3.2 2.5.6 3.6.1.3 0 .7-.2 1z"/></svg>
      </span>
      0438 615 274
    </li>
    <li class="contacts__item">
      <span class="contacts__icon">
        <svg width="12" height="12" viewBox="0 0 24 24" aria-hidden="true"><rect x="2" y="5" width="20" height="14" rx="1" fill="none" stroke="var(--navy)" stroke-width="2.5"/><path d="M2 6l10 7 10-7" fill="none" stroke="var(--navy)" stroke-width="2.5"/></svg>
      </span>
      admin@vrtelectrical.com.au
    </li>
    <li class="contacts__item">
      <span class="contacts__icon">
        <svg width="12" height="12" viewBox="0 0 24 24" aria-hidden="true"><circle cx="12" cy="12" r="9.5" fill="none" stroke="var(--navy)" stroke-width="2.2"/><path d="M2.5 12h19M12 2.5c3 3 3 16 0 19M12 2.5c-3 3-3 16 0 19" fill="none" stroke="var(--navy)" stroke-width="1.8"/></svg>
      </span>
      www.vrtelectrical.com.au
    </li>
  </ul>

  <p class="licence">Licence No. <strong>64193</strong></p>

  <div class="brand brand--front"><span class="brand__dot"></span>VRT Electrical</div>
</section>

<section class="card card--back" aria-label="Business card back">
  <div class="brand brand--back"><span class="brand__dot"></span>VRT Electrical</div>
</section>

</body>
</html>
```